Renata Quisby

Luxury And Style -

Black - White & Gold

Target Market(s)

Fashion

Industry/Entity Type

Fashion

Requirements
Must have
• High-End
Nice to have
• We will Print on Silk Paper

```html
<!DOCTYPE html>
<html lang="en">
<head>
<meta charset="UTF-8">
<title>Renata Quisby — Letterhead</title>
<link rel="stylesheet" href="https://fonts.googleapis.com/css2?family=Arimo:wght@400&family=Tinos:wght@400&display=swap">
<style>
  :root {
    --navy: #010424;
    --paper: #fcfcfc;
    --gold: #c29a66;
    --gold-light: #e2c398;
    --ink: #111111;
    --contact: #ffffff;
  }
  * { margin: 0; padding: 0; box-sizing: border-box; }
  html, body { width: 910px; height: 1200px; overflow: hidden; background: var(--paper); }
  .letterhead { position: relative; width: 910px; height: 1200px; background: var(--paper); overflow: hidden; }

  .header-band {
    position: absolute; left: 11px; top: 10px; width: 887px; height: 164px;
    background: var(--navy);
  }
  .brand-mark {
    position: absolute; left: 103px; top: 24px; width: 64px; height: 64px;
    border: 2px solid var(--gold); border-radius: 50%;
  }
  .brand-name {
    position: absolute; left: 20px; top: 111px; width: 230px; text-align: center;
    font-family: "Tinos", serif; font-size: 19px; letter-spacing: 3.5px;
    color: var(--gold); white-space: nowrap; line-height: 20px;
  }
  .brand-tagline {
    position: absolute; left: 20px; top: 136px; width: 230px; text-align: center;
    font-family: "Tinos", serif; font-size: 8px; letter-spacing: 0.5px;
    color: var(--gold); line-height: 10px;
  }

  .contact {
    position: absolute; left: 639px; top: 35px; height: 118px;
    border-left: 1px solid var(--gold); padding-left: 14px;
    font-style: normal;
  }
  .contact-list { list-style: none; }
  .contact-item {
    display: flex; align-items: flex-start; gap: 15px;
    font-family: "Tinos", serif; font-size: 17.5px; line-height: 20px;
    color: var(--contact); margin-bottom: 3px; white-space: nowrap;
  }
  .contact-item.address { margin-top: 8px; }
  .contact-icon { width: 13px; height: 13px; margin-top: 4px; flex: none; }

  .letter-body {
    position: absolute; left: 140px; top: 393px; width: 637px;
    font-family: "Arimo", sans-serif; font-size: 16.6px; line-height: 19px;
    color: var(--ink); text-align: justify;
  }
  .letter-body p.short-first { margin-bottom: 40px; }
  .letter-body p.long-first { margin-bottom: 43px; }
  .letter-body p.long-second { margin-bottom: 37px; }

  .footer-band {
    position: absolute; left: 0; bottom: 0; width: 910px; height: 110px;
    background: linear-gradient(180deg, var(--paper) 0%, var(--gold-light) 22%, var(--gold) 34%, var(--navy) 62%, var(--navy) 100%);
  }
</style>
</head>
<body>
<main class="letterhead">
  <header class="header-band">
    <span class="brand-mark"></span>
    <div class="brand-name">RENATA QUISBY</div>
    <div class="brand-tagline">LUXURY AND STYLE</div>

    <address class="contact">
      <ul class="contact-list">
        <li class="contact-item">
          <svg class="contact-icon" viewBox="0 0 16 16" aria-hidden="true"><path fill="#c29a66" d="M3.2 1.2l2.4 2.6-1.3 1.8c.9 2 2.5 3.6 4.5 4.6l1.8-1.3 2.6 2.4-1.6 2.4C6.5 13.4 2.4 9.3 1 4.2z"/></svg>
          <span>021-487 305 612</span>
        </li>
        <li class="contact-item">
          <svg class="contact-icon" viewBox="0 0 16 16" aria-hidden="true"><rect x="1" y="3.5" width="14" height="9.5" fill="none" stroke="#c29a66" stroke-width="1.4"/><path d="M1 3.5l7 5.5 7-5.5" fill="none" stroke="#c29a66" stroke-width="1.4"/></svg>
          <span>hello@quisbyatelier.com</span>
        </li>
        <li class="contact-item">
          <svg class="contact-icon" viewBox="0 0 16 16" aria-hidden="true"><circle cx="8" cy="8" r="6.5" fill="none" stroke="#c29a66" stroke-width="1.4"/><path d="M1.5 8h13M8 1.5c-2.4 2.6-2.4 10.4 0 13M8 1.5c2.4 2.6 2.4 10.4 0 13" fill="none" stroke="#c29a66" stroke-width="1.1"/></svg>
          <span>www.quisbyatelier.com</span>
        </li>
        <li class="contact-item address">
          <svg class="contact-icon" viewBox="0 0 16 16" aria-hidden="true"><path fill="#c29a66" d="M8 0.5a5.5 5.5 0 0 0-5.5 5.5c0 4 5.5 9.5 5.5 9.5s5.5-5.5 5.5-9.5A5.5 5.5 0 0 0 8 .5zm0 7.7a2.2 2.2 0 1 1 0-4.4 2.2 2.2 0 0 1 0 4.4z"/></svg>
          <span>87, Calder Row<br>Northvale, 30418</span>
        </li>
      </ul>
    </address>
  </header>

  <section class="letter-body">
    <p class="short-first">Lorem ipsum dolor sit amet, consectetur adipiscing elit. Donec fringilla neque euismod volutpat cursus. Vestibulum ac pretium orci, consequat elementum velit. Etiam bibendum purus ac augue finibus volutpat. Vestibulum justo nisl</p>
    <p class="long-first">Lorem ipsum dolor sit amet, consectetur adipiscing elit. Donec fringilla neque euismod volutpat cursus. Vestibulum ac pretium orci, consequat elementum velit. Etiam bibendum purus ac augue finibus volutpat. Vestibulum justo nisl, gravida aliquet sollicitudin ut, finibus vitae mi. Praesent aliquet scelerisque blandit. Sed id varius lacus, id tristique sem. Fusce et lobortis leo. Aliquam mollis pellentesque magna, condimentum ullamcorper ex ullamcorper non. Morbi ultricies nunc eu tellus dignissim, eget venenatis dolor ullamcorper. Etiam dolor eros, iaculis at ultricies nec, volutpat nec orci. Vivamus tincidunt rutrum sapien, ac porttitor mauris tristique nec.</p>
    <p class="long-second">Lorem ipsum dolor sit amet, consectetur adipiscing elit. Donec fringilla neque euismod volutpat cursus. Vestibulum ac pretium orci, consequat elementum velit. Etiam bibendum purus ac augue finibus volutpat. Vestibulum justo nisl, gravida aliquet sollicitudin ut, finibus vitae mi. Praesent aliquet scelerisque blandit. Sed id varius lacus, id tristique sem. Fusce et lobortis leo. Aliquam mollis pellentesque magna, condimentum ullamcorper ex ullamcorper non. Morbi ultricies nunc eu tellus dignissim, eget venenatis dolor ullamcorper. Etiam dolor eros, iaculis at ultricies nec, volutpat nec orci. Vivamus tincidunt rutrum sapien, ac porttitor mauris tristique nec.</p>
    <p>Lorem ipsum dolor sit amet, consectetur adipiscing elit. Donec fringilla neque euismod volutpat cursus. Vestibulum ac pretium orci, consequat elementum velit. Etiam bibendum purus ac augue finibus volutpat. Vestibulum justo nisl</p>
  </section>

  <div class="footer-band" role="img" aria-label="Decorative footer band in navy and gold"></div>
</main>
</body>
</html>
```